Upstart Retirement Planning Firm needs help with business card design

Harborlight Wealth Partners, LLC is looking for help with business card design. We give advice on investments, insurance, and other financial matters related to retirement. There are some required disclosures that we will provide but mostly we are looking for a professional, classy business card that reflects the theme we have chosen. We have a logo that is attached but we would like to add a phrase; "Turning Your Earned Income Into Retirement Income"

Doubled sided only so that we can add the required disclosures (needed for our industry) on the back of the card. We will provide the exact words for this in 1-2 days.

Target Market(s)

Retirees and Pre-retirees. Professionals 50+ years old

Industry/Entity Type

Financial Planning

Contact Information for Business Card

We currently have two people who will need separate cards so we'd like to have a template so that we can add names for new cards in the future.

For the first run, please show the following information.

Neil Osgood, MBA, ChFC®, CLU®
Financial Advisor, Registered Representative
nosgood@harborlightwp.example
Phone: (555) 218-3960
Toll Free Fax: (555) 218-3961

Address is
2876 Meadowbrook Pkwy.
Suite K418
Virginia Beach, VA 23019

Colors
3277b5

Requirements
Must have
• Logo, contact info, small phase to describe business (in description), required legal disclosures on back of the card as follows (in small font)
• Neil Osgood is a registered representative of and offers securities through Brightwater Capital Brokerage Corporation, Member SIPC. Brightwater Capital Brokerage Corporation is a member of the Brightwater Advisory Group which is the marketing name for Brightwater Holding Corporation and its affiliates.
Nice to have
• Rounded edges, raised letters
Should not have
• any colors that aren't in the logo (other than black for font)

```html
<!DOCTYPE html>
<html lang="en">
<head>
<meta charset="utf-8">
<title>Harborlight Wealth Partners – Business Card</title>
<link rel="stylesheet" href="https://fonts.googleapis.com/css2?family=Arimo:wght@400;700&display=swap">
<style>
  :root {
    --brand-blue: #1a6fbd;
    --brand-blue-deep: #0f62b0;
    --ink: #1d1d1d;
    --rule-grey: #9a9a9a;
    --paper: #ffffff;
    --stage: #e9eaec;
  }
  * { box-sizing: border-box; margin: 0; padding: 0; }
  html, body { width: 1200px; height: 750px; overflow: hidden; }
  body {
    background: var(--stage);
    font-family: "Arimo", Arial, sans-serif;
    position: relative;
  }
  .card {
    position: absolute;
    width: 540px;
    height: 309px;
    border-radius: 8px;
    overflow: hidden;
    box-shadow: 0 6px 18px rgba(0,0,0,0.18);
  }
  /* Front */
  .card-front {
    left: 60px; top: 70px;
    background: var(--brand-blue);
    color: var(--paper);
    display: flex; flex-direction: column; align-items: center; justify-content: center;
  }
  .card-front .wordmark {
    font-size: 30px; font-weight: 700; letter-spacing: 0.5px; text-align: center; line-height: 1.2;
  }
  .card-front .wordmark-sub {
    font-size: 13px; letter-spacing: 4px; margin-top: 6px;
  }
  .card-front .tagline {
    margin-top: 46px; font-size: 15px; letter-spacing: 0.3px;
  }
  /* Back */
  .card-back {
    left: 600px; top: 370px;
    background: var(--paper);
    color: var(--ink);
  }
  .card-back .wordmark {
    position: absolute; right: 28px; top: 30px; width: 260px;
    text-align: right; color: var(--brand-blue);
    font-size: 21px; font-weight: 700; line-height: 1.2;
  }
  .card-back .wordmark-sub {
    display: block; font-size: 11px; letter-spacing: 3px; margin-top: 4px;
  }
  .card-back .address-rule {
    position: absolute; right: 28px; top: 112px; width: 230px;
    border-top: 1px solid var(--rule-grey);
  }
  .card-back .address {
    position: absolute; right: 28px; top: 124px;
    text-align: right; font-size: 13px; line-height: 1.45; font-style: normal;
  }
  .card-back .person { position: absolute; left: 30px; top: 168px; width: 300px; }
  .card-back .person-name {
    color: var(--brand-blue); font-size: 20px; font-weight: 700;
  }
  .card-back .person-credentials { font-size: 12px; font-weight: 700; }
  .card-back .person-title { font-size: 12px; margin-top: 4px; }
  .card-back .person-rule { border-top: 1px solid var(--rule-grey); width: 270px; margin-top: 8px; }
  .card-back .contact-list { list-style: none; margin-top: 6px; font-size: 12.5px; line-height: 1.5; }
  .card-back .contact-list li { display: flex; align-items: center; gap: 8px; }
  .card-back .contact-list svg { width: 13px; height: 13px; fill: var(--brand-blue-deep); flex: none; }
  .card-back .foot-line {
    position: absolute; left: 0; right: 0; bottom: 15px; border-top: 1px solid #c8c8c8;
  }
  .card-back .foot-band {
    position: absolute; left: 0; right: 0; bottom: 0; height: 12px; background: var(--brand-blue);
  }
</style>
</head>
<body>
  <section class="card card-front">
    <div class="wordmark">Harborlight Wealth Partners</div>
    <div class="wordmark-sub">L L C</div>
    <p class="tagline">Turning Your Earned Income Into Retirement Income</p>
  </section>

  <section class="card card-back">
    <div class="wordmark">Harborlight Wealth Partners<span class="wordmark-sub">L L C</span></div>
    <div class="address-rule"></div>
    <address class="address">
      2876 Meadowbrook Pkwy.<br>
      Suite K418<br>
      Virginia Beach, VA 23019
    </address>

    <div class="person">
      <div><span class="person-name">Neil Osgood,</span> <span class="person-credentials" style="color: var(--brand-blue);">MBA, ChFC®, CLU®</span></div>
      <div class="person-title">Financial Advisor, Registered Representative</div>
      <div class="person-rule"></div>
      <ul class="contact-list">
        <li><svg viewBox="0 0 16 16" aria-hidden="true"><path d="M3 6c0-2 2-3 5-3s5 1 5 3l-2 1-1-2H6L5 7z M4 8h8l1 5H3z"/></svg>(555) 218-3960</li>
        <li><svg viewBox="0 0 16 16" aria-hidden="true"><path d="M3 6c0-2 2-3 5-3s5 1 5 3l-2 1-1-2H6L5 7z M4 8h8l1 5H3z"/></svg>(555) 218-3961 (Toll Free)</li>
        <li><svg viewBox="0 0 16 16" aria-hidden="true"><path d="M1 4h14v9H1z" fill="none"/><path d="M1 4h14v1.2L8 9.5 1 5.2z M1 6.6l7 4.3 7-4.3V13H1z"/></svg>nosgood@harborlightwp.example</li>
      </ul>
    </div>

    <div class="foot-line"></div>
    <div class="foot-band"></div>
  </section>
</body>
</html>
```